Information Prospectus for education sector

We need to create a 12 page information memorandum reagrding the education an industry snapshot in Australia, This will be sent to investors in Australia and overseas looking to invest into the education sector in Australia.

Target Market(s)

Investors into the education sector

Industry/Entity Type

Education

Font styles to use
Sans Serif

Colors
fbee3d
33a6d7
9bcb3c

```html
<!DOCTYPE html>
<html lang="en">
<head>
<meta charset="utf-8">
<title>International Education Industry Snapshot – Page Spreads</title>
<link rel="stylesheet" href="https://fonts.googleapis.com/css2?family=Oswald:wght@400;500&family=Montserrat:wght@400;600;700&display=swap">
<style>
:root{
  --yellow:#fbee3d;
  --blue:#33a6d7;
  --green:#9bcb3c;
  --green-dark:#6a9a1f;
  --blue-dark:#1f7fbf;
  --ink:#333;
  --ink-soft:#555;
  --board:#c2c2c2;
  --grey-band:#8a8a8a;
  --info-yellow:#f8f088;
  --info-blue:#a9dcf1;
}
*{box-sizing:border-box;margin:0;padding:0}
html,body{width:1200px;height:1008px;overflow:hidden}
body{background:var(--board);position:relative;font-family:'Montserrat',sans-serif;color:var(--ink)}
.board-label{position:absolute;width:500px;text-align:center;font-family:'Montserrat',sans-serif;font-size:24px;font-weight:400;color:#222;letter-spacing:.5px}
.page{position:absolute;width:500px;height:354px;background:#fff;overflow:hidden;box-shadow:0 14px 14px -8px rgba(0,0,0,.35)}
.abs{position:absolute}
.page-header,.page-footer-shape{position:absolute;left:0;top:0}
.footer-band{position:absolute;left:0;bottom:0;width:100%;height:24px;background:var(--blue)}
.footer-url{position:absolute;left:0;bottom:5px;width:100%;text-align:center;color:#fff;font-size:8px;letter-spacing:1px}
.office-mark{position:absolute;right:10px;text-align:center;font-family:'Montserrat',sans-serif;font-weight:600;color:#1d2a33;line-height:1.25;white-space:nowrap}
.office-mark .rule{display:block;height:1px;background:#1d2a33;margin:2px 0}
.office-mark .dot{display:block;margin:0 auto 3px;width:14px;height:14px;border-radius:50%;background:#1d2a33}
.heading-green{font-family:'Oswald',sans-serif;font-weight:500;color:var(--green-dark);text-transform:uppercase}
.body-text{font-size:7px;line-height:1.42;color:var(--ink-soft);text-align:justify}
.body-text p{margin-bottom:4px}
/* cover */
.cover-grey{position:absolute;left:0;top:0;width:100%;height:243px;background:var(--grey-band)}
.cover-title{position:absolute;left:14px;top:268px;font-family:'Oswald',sans-serif;font-weight:500;font-size:21px;line-height:1.1;color:#222;letter-spacing:-.2px}
.cover-title .sub{display:block;color:var(--blue-dark);font-weight:400}
.cover-title .by{display:block;font-family:'Montserrat',sans-serif;font-size:6.5px;color:#666;letter-spacing:1px;margin-top:2px;font-weight:400}
.cover-footer{position:absolute;left:0;bottom:0;width:100%;height:21px;background:var(--grey-band)}
/* page 1 */
.bullet-list{list-style:none}
.bullet-list li{position:relative;padding-left:10px}
.bullet-list li::before{content:"";position:absolute;left:0;top:3px;width:4px;height:4px;border-radius:50%;background:#111}
.check-list{list-style:none;font-size:7.2px;color:var(--ink-soft);line-height:1.9}
.check-list li{position:relative;padding-left:10px}
.check-list li::before{content:"";position:absolute;left:0;top:3px;width:5px;height:5px;border:1px solid var(--green)}
/* infographic */
.info-map{background:var(--info-yellow)}
.info-row{position:absolute;left:0;width:206px;height:19px;background:var(--info-blue);border-top:1px dashed #fff;font-size:5.3px;line-height:1.35;color:#345;display:flex;align-items:center;gap:6px;padding:0 6px}
.info-row .icon{flex:none;width:26px;height:10px;background:var(--blue-dark);border-radius:2px}
.info-row .text{flex:1}
.caption{font-size:5.5px;color:#555}
.chart-title{font-size:6.6px;font-weight:600;color:#222}
</style>
</head>
<body>

<div class="board-label" style="left:70px;top:60px">COVER PAGE</div>
<div class="board-label" style="left:619px;top:60px">INNER PAGE-1</div>
<div class="board-label" style="left:82px;top:908px">INNER PAGE-2</div>
<div class="board-label" style="left:610px;top:908px">INNER PAGE-3</div>

<!-- Cover page -->
<section class="page cover" style="left:82px;top:101px">
  <div class="cover-grey"></div>
  <svg class="abs" style="left:0;top:0" width="500" height="260" viewBox="0 0 500 260" role="img" aria-label="Photograph of a modern glass office building against a blue sky, tinted with a green diagonal overlay">
    <defs>
      <linearGradient id="photoTone" x1="0" y1="0" x2="1" y2="1">
        <stop offset="0" stop-color="#8cc8ea"/>
        <stop offset=".55" stop-color="#3f7fb0"/>
        <stop offset="1" stop-color="#8fc23a"/>
      </linearGradient>
    </defs>
    <polygon points="0,37 421,37 310,260 0,260" fill="url(#photoTone)"/>
    <polygon points="421,37 310,260 130,260 340,150" fill="var(--green)" opacity=".7"/>
  </svg>
  <svg class="abs" style="left:0;top:0" width="500" height="260" viewBox="0 0 500 260">
    <polygon points="310,260 500,230 500,260" fill="#fff"/>
  </svg>
  <h1 class="cover-title">THE INTERNATIONAL EDUCATION<span class="sub">INDUSTRY SNAPSHOT</span><span class="by">KESTREL CORP</span></h1>
  <div class="office-mark" style="top:256px;right:22px;width:150px;font-size:7.5px">
    <span class="dot" style="width:20px;height:20px"></span>National Education Office<span class="rule"></span><span style="font-size:7px">Learning and Skills Division</span>
  </div>
  <div class="cover-footer"></div>
  <div class="footer-url" style="bottom:5px">www.kestrelcorp.com.au</div>
</section>

<!-- Inner page 1 -->
<section class="page" style="left:619px;top:101px">
  <svg class="page-header" width="500" height="60" viewBox="0 0 500 60">
    <polygon points="0,0 225,0 245,20 75,46 0,12" fill="var(--green)"/>
    <polygon points="222,0 500,0 500,6 245,40" fill="var(--yellow)"/>
  </svg>
  <div class="abs body-text" style="left:20px;top:84px;width:460px">
    <ul class="bullet-list">
      <li>
        <p>KESTREL CORP is an independent and Australian owned agency providing premium specialist services to investors, buyers and sellers across the private education markets.</p>
        <p>Our team consists of people with a long-term successful career in the education industry. The team is a knowledgeable and informed group of professionals with a strong commitment and attitude which allows us to professionally drive negotiations.</p>
        <p>In the first six months of 2018, we have successfully completed many transactions in the sale of international education institutes. We currently have investment and acquisition opportunities from $1m to $15m.</p>
      </li>
    </ul>
  </div>
  <div class="abs" style="left:20px;top:186px;width:440px">
    <h2 class="heading-green" style="font-size:11.5px;font-weight:400;line-height:1.5;padding-left:10px;position:relative"><span style="position:absolute;left:0;top:6px;width:4px;height:4px;border-radius:50%;background:#111"></span>Throughout this presentation, prospective investors will have an<br>insight knowledge of:</h2>
    <ul class="check-list" style="margin-top:3px">
      <li>The outlook and growth of International Education Industry in Australia</li>
      <li>Investment opportunity of International Education Industry in Australia</li>
      <li>Investment return and risks</li>
    </ul>
  </div>
  <svg class="page-footer-shape" style="top:290px" width="500" height="64" viewBox="0 0 500 64">
    <polygon points="405,0 500,0 500,64 380,64" fill="var(--blue)"/>
  </svg>
  <div class="footer-band"></div>
  <div class="office-mark" style="top:296px;width:100px;font-size:5.6px"><span class="dot"></span>National Education Office<span class="rule"></span>Learning and Skills Division</div>
  <div class="footer-url">www.kestrelcorp.com.au</div>
</section>

<!-- Inner page 2 -->
<section class="page" style="left:82px;top:517px">
  <svg class="page-header" width="500" height="90" viewBox="0 0 500 90">
    <polygon points="0,0 350,0 385,12 82,46 0,8" fill="var(--green)"/>
    <polygon points="345,0 500,0 500,83 385,12" fill="var(--yellow)"/>
  </svg>
  <h2 class="abs heading-green" style="left:20px;top:88px;font-size:10px">International Education Industry in Australia</h2>
  <div class="abs body-text" style="left:20px;top:113px;width:232px">
    <p>In 2016-2017, the Education Industry generated $28.6 Billion to the Australian Economy and was the third largest source of export income for Australia after Iron and Coal. It increased 16.1% compared to 2015-2016 Financial Year which was $24.145 Billion. The growth in Education Export has been very sustainable with the average growth of 11% in the last 5 years.</p>
    <p style="margin-top:7px">The higher education sector generated $19.1 billion in export income (68.1% of total on-shore earnings). The VET sector generated $4.8 billion in earnings (17.3% of total), ELICOS was $1.4 billion (5.2%); schools was $1.2 billion (4.4%); and non-award was $981 million (3.5%).</p>
  </div>
  <h2 class="abs heading-green" style="left:318px;top:86px;font-size:11px">Business Opportunities</h2>
  <div class="abs" style="left:280px;top:115px;width:206px;height:160px">
    <div class="abs info-map" style="left:0;top:0;width:206px;height:80px" role="img" aria-label="Map of Australia showing 2016-17 export income by state and territory; education worth 28.6 billion to the economy"></div>
    <div class="info-row" style="top:80px"><span class="icon"></span><span class="text">Education is the <b>3rd largest export</b> for Australia</span></div>
    <div class="info-row" style="top:99px"><span class="icon"></span><span class="text">International Education supports <b>130,000 jobs</b> nationally</span></div>
    <div class="info-row" style="top:118px"><span class="icon"></span><span class="text"><b>China 28% India 11%</b> are the largest sources of international student in 2016</span></div>
    <div class="info-row" style="top:137px;height:22px"><span class="icon"></span><span class="text">43% of international enrolments in 2016 are in <b>higher education</b> and 26% in <b>Vocational Education and training</b></span></div>
  </div>
  <div class="abs caption" style="left:292px;top:279px">Sourced from The National Education Office</div>
  <svg class="page-footer-shape" style="top:290px" width="500" height="64" viewBox="0 0 500 64">
    <polygon points="405,0 500,0 500,64 380,64" fill="var(--blue)"/>
  </svg>
  <div class="footer-band"></div>
  <div class="office-mark" style="top:296px;width:100px;font-size:5.6px"><span class="dot"></span>National Education Office<span class="rule"></span>Learning and Skills Division</div>
  <div class="footer-url">www.kestrelcorp.com.au</div>
</section>

<!-- Inner page 3 -->
<section class="page" style="left:619px;top:517px">
  <svg class="page-header" width="500" height="60" viewBox="0 0 500 60">
    <polygon points="0,0 225,0 245,20 75,46 0,12" fill="var(--green)"/>
    <polygon points="222,0 500,0 500,6 245,40" fill="var(--yellow)"/>
  </svg>
  <h2 class="abs heading-green" style="left:26px;top:62px;font-size:11.5px">Business Opportunities</h2>
  <div class="abs body-text" style="left:26px;top:83px;width:450px;text-align:left">
    <p style="margin-bottom:2px">The International Education Industry is non arguably one of the key forces to drive the Australian Economy for now and in the future.</p>
    <p>Australia has established itself as the global leader in the provision of international education. Its comparative strength – that is, the ‘Australian Advantage’ – has been integral to our performance to this point, and will be key to the sector’s future successes.</p>
  </div>
  <div class="abs chart-title" style="left:33px;top:155px">Onshore in Australia: Export income from Education Services</div>
  <svg class="abs" style="left:26px;top:166px" width="220" height="120" viewBox="0 0 220 120" font-family="Montserrat, sans-serif" font-size="5.5" fill="#222">
    <text x="0" y="54" transform="rotate(-90 4 52)" font-size="5">$ Billion</text>
    <g text-anchor="end">
      <text x="19" y="9">30.0</text><text x="19" y="24.5">25.0</text><text x="19" y="40">20.0</text>
      <text x="19" y="55.5">15.0</text><text x="19" y="71">10.0</text><text x="19" y="86.5">5.0</text><text x="19" y="102">0.0</text>
    </g>
    <line x1="22" y1="7" x2="22" y2="100" stroke="#222" stroke-width=".6"/>
    <line x1="22" y1="100" x2="215" y2="100" stroke="#222" stroke-width=".6"/>
    <g fill="var(--blue)">
      <rect x="30" y="47.6" width="10" height="52.4"/>
      <rect x="63" y="42.7" width="10" height="57.3"/>
      <rect x="96" y="34" width="10" height="66"/>
      <rect x="129" y="25.3" width="10" height="74.7"/>
      <rect x="162" y="13.2" width="10" height="86.8"/>
    </g>
    <g text-anchor="middle" font-weight="600">
      <text x="35" y="44">16.9</text><text x="68" y="39">18.5</text><text x="101" y="30">21.3</text><text x="134" y="22">24.1</text><text x="167" y="9.5">28.0</text>
      <text x="35" y="110">2012-23</text><text x="68" y="110">2013-14</text><text x="101" y="110">2014-15</text><text x="134" y="110">2015-16</text><text x="167" y="110">2016-17</text>
    </g>
  </svg>
  <div class="abs chart-title" style="left:270px;top:154px">Export Income by State and Territory, 2016-17</div>
  <div class="abs" style="left:262px;top:168px;width:150px;height:105px;background:linear-gradient(135deg,var(--blue) 0%,var(--green) 55%,var(--yellow) 100%);border-radius:28px 40px 30px 20px" role="img" aria-label="Map of Australia coloured by state with export income labels for each state and territory"></div>
  <div class="abs caption" style="left:267px;top:278px">Sourced from the National Statistics Bureau</div>
  <svg class="page-footer-shape" style="top:290px" width="500" height="64" viewBox="0 0 500 64">
    <polygon points="405,0 500,0 500,64 380,64" fill="var(--blue)"/>
  </svg>
  <div class="footer-band"></div>
  <div class="office-mark" style="top:296px;width:100px;font-size:5.6px"><span class="dot"></span>National Education Office<span class="rule"></span>Learning and Skills Division</div>
  <div class="footer-url">www.kestrelcorp.com.au</div>
</section>

</body>
</html>
```